Business Card Design Project - Brindle Media

We need a new business card that fits with our new logo. We are a social media agency and consultancy operating in China. We want a fresh and strong business card. Our cards need to be two-sided as we have both English and Chinese language names and addresses on the card, but as with our current business card this does not need to be a mirror-image. Our thoughts go out to a white card on the front where the logo/name is and then using the logo colours for different coloured back-grounds. i.e that the back of the biz card works with the four different colours in the logo.

Attached is the new logo, and also a copy of our old business cards.

Target Market(s)

CEO's, CMO's. media and advertising professionals

Industry/Entity Type

Business

Requirements
Must have
• inclusion of both Chinese and English language
Nice to have
• four different colored versions of the back of the biz card. Our logo has four colors and each of these colors we would like to have a version of.

```html
<!DOCTYPE html>
<html lang="en">
<head>
<meta charset="utf-8">
<title>Brindle Media – Business Card</title>
<link rel="stylesheet" href="https://fonts.googleapis.com/css2?family=Saira:wght@400;500;700&family=Noto+Sans+SC:wght@400;500&display=swap">
<style>
  :root {
    --brand-green: #8dc63f;
    --brand-purple: #662d91;
    --brand-magenta: #ec008c;
    --brand-orange: #f26522;
    --ink: #111111;
    --ink-soft: #3a3a3a;
    --paper: #ffffff;
    --stage: #ffffff;
  }
  * { margin: 0; padding: 0; box-sizing: border-box; }
  html, body {
    width: 1200px; height: 925px; overflow: hidden;
    background: var(--stage);
    font-family: "Saira", sans-serif;
  }
  .stage { position: relative; width: 1200px; height: 925px; }

  .card {
    position: absolute; top: 85px;
    width: 474px; height: 777px;
    overflow: hidden;
    box-shadow: 6px 10px 16px rgba(0,0,0,0.28);
  }
  .card--front { left: 93px; background: var(--paper); border-top-right-radius: 66px; }
  .card--back { left: 645px; background: var(--brand-green); border-top-left-radius: 66px; color: var(--paper); }

  .wordmark {
    position: absolute; left: 30px; top: 40px;
    font-family: "Saira", sans-serif; font-weight: 700;
    font-size: 76px; line-height: 0.95; letter-spacing: -1px;
    white-space: nowrap;
  }
  .wordmark span { display: block; }
  .wordmark .wordmark__second { padding-left: 150px; }
  .card--front .wordmark { color: var(--ink); }
  .card--back .wordmark { color: var(--paper); left: 28px; }
  .wordmark-square {
    position: absolute; width: 18px; height: 18px; top: 105px; left: 430px;
    background: var(--brand-orange);
  }
  .card--back .wordmark-square { background: var(--paper); left: 428px; }

  .person { position: absolute; left: 28px; top: 345px; white-space: nowrap; }
  .person__name { font-size: 60px; font-weight: 400; color: var(--ink); line-height: 1; letter-spacing: -0.5px; }
  .person__role { font-size: 30px; font-weight: 400; color: var(--ink-soft); line-height: 1.05; margin-top: 2px; }

  .contacts {
    position: absolute; left: 28px; top: 460px;
    display: grid; grid-template-columns: 92px auto; row-gap: 0;
    font-size: 20px; font-weight: 500; line-height: 1.25;
  }
  .contacts dt { color: var(--brand-green); }
  .contacts dd { color: var(--ink-soft); }

  .colour-bars { position: absolute; left: 25px; top: 716px; display: flex; gap: 4px; }
  .colour-bars span { width: 103px; height: 35px; }
  .bar--green { background: var(--brand-green); }
  .bar--purple { background: var(--brand-purple); }
  .bar--magenta { background: var(--brand-magenta); }
  .bar--orange { background: var(--brand-orange); }

  .cn-name { position: absolute; left: 22px; top: 340px; font-family: "Noto Sans SC", sans-serif; display: flex; align-items: baseline; gap: 22px; white-space: nowrap; }
  .cn-name__name { font-size: 54px; font-weight: 500; letter-spacing: 3px; }
  .cn-name__role { font-size: 25px; font-weight: 400; letter-spacing: 2px; }

  .address { position: absolute; left: 22px; top: 447px; font-size: 14.5px; font-weight: 500; line-height: 1.35; white-space: nowrap; }
  .address--cn { font-family: "Noto Sans SC", sans-serif; font-size: 13.5px; }
  .address--en { top: 500px; font-family: "Saira", sans-serif; }

  .website { position: absolute; left: 22px; top: 704px; font-size: 40px; font-weight: 400; letter-spacing: -0.3px; white-space: nowrap; }
</style>
</head>
<body>
<main class="stage">
  <section class="card card--front" aria-label="Card front">
    <div class="wordmark"><span>Brindle</span><span class="wordmark__second">Media</span></div>
    <div class="wordmark-square" aria-hidden="true"></div>

    <div class="person">
      <h1 class="person__name">Owen Hartley</h1>
      <p class="person__role">managing director</p>
    </div>

    <dl class="contacts">
      <dt>email:</dt><dd>owen@hartley.com</dd>
      <dt>chat:</dt><dd>owenbeijing</dd>
      <dt>mobile:</dt><dd>+86 13800452187</dd>
    </dl>

    <div class="colour-bars" aria-hidden="true">
      <span class="bar--green"></span><span class="bar--purple"></span><span class="bar--magenta"></span><span class="bar--orange"></span>
    </div>
  </section>

  <section class="card card--back" aria-label="Card back">
    <div class="wordmark"><span>Brindle</span><span class="wordmark__second">Media</span></div>
    <div class="wordmark-square" aria-hidden="true"></div>

    <div class="cn-name">
      <span class="cn-name__name">何欧文</span>
      <span class="cn-name__role">董事总经理</span>
    </div>

    <p class="address address--cn">红桥商务中心 套房C310 红桥商务中心套房C310<br>东风南中路东风南路东风南路朝阳区 · 北京 (100026)</p>
    <p class="address address--en">Suite C310, Hong Qiao Business Centre<br>Dongfeng South Rd Chaoyang District, Beijing 100026</p>

    <p class="website">www.brindlechina.com</p>
  </section>
</main>
</body>
</html>
```